Company or website name
- Jardin d'Aurores
- Slogan or Tagline
- No Taglines, but each description listed here needs to be on the front label of each of these wines.
- Describe your company and organization and target audience
- Consumers buying wine aged 30+, restaurants. Of wine buyers, 55% are female shopping at major grocery chains.
- The design should have the following
- The style should marry traditional sophistication with a touch of contemporary fun. It should tell knowledgeable wine buyers that it is a serious, quality product, but have enough light to attract the novice wine buyers and impulse buyers. Must have: 1) Jardin d'Aurores (brand name) 2) Method Traditionelle 3) Appellation Cremant de Limoux Controlee 4) Product of France -Brut -Brut RoseFountaine de la Vie means "Garden of Dawns" in French We would like this idea implemented into the design of the label. As a sparkling wine, bubbles are what spring from this fountain.
- This design should not have this in the entries
- No use of Gold or Gold Foil (scratches too easily). Also, black labels tend to scuff and don't travel well (plus they don't stand out on the shelves as much). Not too frilly – this is a quality product. We do not want to turn off serious wine buyers because they don’t take the label seriously.

```html
<!DOCTYPE html>
<html lang="en">
<head>
<meta charset="utf-8">
<title>Jardin d'Aurores – Crémant de Limoux Label</title>
<link rel="stylesheet" href="https://fonts.googleapis.com/css2?family=Dancing+Script:wght@700&family=Libre+Baskerville:wght@400;700&display=swap">
<style>
  :root {
    --page: #ffffff;
    --rim-dark: #2c2f95;
    --rim-light: #4a4fc0;
    --label-light: #fbf9f1;
    --label-mid: #f3f0e3;
    --label-shade: #e6e2d2;
    --ink-blue: #3a3db0;
    --ink-blue-deep: #2c2f95;
    --ink-slate: #4a4f6e;
  }
  html, body {
    margin: 0;
    padding: 0;
    width: 1200px;
    height: 960px;
    overflow: hidden;
    background: var(--page);
  }
  .canvas {
    position: relative;
    width: 1200px;
    height: 960px;
  }
  .label {
    position: absolute;
    left: 228px;
    top: 30px;
    width: 744px;
    height: 900px;
    border-radius: 50%;
    background: linear-gradient(90deg, var(--rim-dark), var(--rim-light) 50%, var(--rim-dark));
  }
  .label-face {
    position: absolute;
    inset: 12px;
    border-radius: 50%;
    background: radial-gradient(ellipse at 55% 40%, var(--label-light) 0%, var(--label-mid) 60%, var(--label-shade) 100%);
  }
  .ornament {
    position: absolute;
    left: 50%;
    transform: translateX(-50%);
    background: linear-gradient(180deg, var(--ink-blue), var(--ink-blue-deep));
    opacity: 0.85;
  }
  .ornament-crest {
    top: 62px;
    width: 250px;
    height: 226px;
    border-radius: 46% 46% 30% 30%;
  }
  .ornament-divider {
    top: 690px;
    width: 220px;
    height: 38px;
    border-radius: 19px;
  }
  .brand-name {
    position: absolute;
    left: 0;
    right: 0;
    margin: 0;
    text-align: center;
    font-family: "Dancing Script", cursive;
    font-weight: 700;
    color: var(--ink-blue);
    line-height: 1;
  }
  .brand-line-1 { top: 318px; font-size: 122px; padding-right: 30px; }
  .brand-line-2 { top: 440px; font-size: 108px; padding-left: 40px; }
  .appellation,
  .method,
  .style-name,
  .origin {
    position: absolute;
    left: 0;
    right: 0;
    margin: 0;
    text-align: center;
    font-family: "Libre Baskerville", serif;
    font-weight: 400;
    color: var(--ink-slate);
    text-transform: uppercase;
    line-height: 1.2;
  }
  .appellation { top: 606px; font-size: 21px; letter-spacing: 1px; }
  .method { top: 644px; font-size: 22px; letter-spacing: 2px; }
  .style-name { top: 746px; font-size: 26px; letter-spacing: 4px; color: var(--ink-blue); }
  .origin { top: 812px; font-size: 18px; letter-spacing: 2px; }
</style>
</head>
<body>
  <main class="canvas">
    <section class="label" aria-label="Jardin d'Aurores sparkling wine front label">
      <div class="label-face">
        <div class="ornament ornament-crest" role="img" aria-label="Blue fountain-like flourish crest ornament"></div>
        <h1 class="brand-name brand-line-1">Jardin</h1>
        <p class="brand-name brand-line-2">d'Aurores</p>
        <p class="appellation">Appellation Cremant de Limoux Controlee</p>
        <p class="method">Method Traditionelle</p>
        <div class="ornament ornament-divider" role="img" aria-label="Blue flourish divider ornament"></div>
        <p class="style-name">Brut</p>
        <p class="origin">Product of France</p>
      </div>
    </section>
  </main>
</body>
</html>
```